依頼詳細
2008年から発行を続けている当社唯一の社外報「未来TSUBASA報」の
1面に掲載するタイトル(見出し部分)のデザインを依頼いたします。
(添付参照:現在のタイトル)

〇未来TSUBASA報
・A4 8ページものの新聞
・知財関連のニュースやイベント、当社製品の紹介などを掲載
・年2度(6/11月)発行
・配布は印刷/データ(現在はデータの方が多い)

〇希望イメージ
・これまでの「真面目な」「由緒ある」といった印象だけではなく
「親しみやすさ」や「身近さ」「明るさ」「元気の良さ」「スタイリッシュさ」を伝えられる紙面にしたい
・読者は企業の知財部の方々なので子供っぽいデザインは避けたい
・企業カラーの緑色をベースにしたい

また、選ばせていただいたデザインをご提案いただいたデザイナー様には
続けてサブ見出し(1面以降のすべての紙面 上部中央に掲載する小さなもの)も
依頼させていただきたいと考えております。

以上、どうぞよろしくお願いいたします。
記載項目
〇タイトル
・1面に掲載
・掲載サイズ:W188mm H76.6㎜
・入れていただきたい事項
①弊社所在地等の情報
第〇号
発行日(例:2022年3月23日)
発行 株式会社青葉企画舎
https://www.aobakikakusha-news.jp/
東京 中央区日本橋浜町3-5-8 TEL:03-4417-2968
大阪 大阪市西区江戸堀3-7-21 TEL:06-7142-8867
名古屋 安城市御幸本町4-16-8 TEL:0566-47-2139
②掲載記事のタイトルを記入できるスペース(W50mmH35.2mmほど)
希望イメージ
シンプル 複雑
単色 カラフル
暗い 明るい
日常 高級
遊び心 厳粛
未来的 伝統的
女性的 男性的
希望する色
青系、緑系
納品ファイル
• イラストレーター形式 (.ai)
補足説明
■ 選んだ理由

弊社の希望する明るさ、爽やかさと知的財産を素敵に融合いただいたと感じました。
ご提案いただいた際の丁寧な文章も決め手の1つでした。

■ 提案者全員のお礼・コメント

曖昧な依頼にも関わらず、たくさんのご提案をいただけ幸甚に存じます。
素敵なデザインばかりで今後の勉強にもさせていただきました。
1つしか当選にできず、心苦しい思いです。
この度は誠にありがとうございました。
皆様の益々のご活躍を祈念いたします。

```html
<!DOCTYPE html>
<html lang="ja">
<head>
<meta charset="utf-8">
<title>未来TSUBASA報 第27号 タイトル</title>
<link rel="stylesheet" href="https://fonts.googleapis.com/css2?family=Noto+Sans+JP:wght@500;700;900&family=M+PLUS+Rounded+1c:wght@800&display=swap">
<style>
  :root {
    --green-deep: #138a3a;
    --green-mid: #2fae45;
    --green-light: #8fd24a;
    --lime: #c8e63c;
    --yellow: #f2e61c;
    --white: #ffffff;
    --ink: #2b2b2b;
    --star: #3aa63a;
    --title: #ffffff;
  }
  * { margin: 0; padding: 0; box-sizing: border-box; }
  html, body { width: 1200px; height: 488px; overflow: hidden; }
  body { font-family: "Noto Sans JP", sans-serif; }
  .masthead {
    position: relative;
    width: 1200px; height: 488px;
    background: linear-gradient(115deg, var(--green-light) 0%, var(--green-mid) 40%, var(--green-deep) 70%, var(--green-mid) 100%);
    overflow: hidden;
  }
  .masthead__texture {
    position: absolute; inset: 0;
    background: linear-gradient(160deg, rgba(255,255,255,0.12) 0%, rgba(255,255,255,0) 45%, rgba(0,60,20,0.18) 100%);
  }
  .title {
    position: absolute; left: 58px; top: 14px;
    font-family: "M PLUS Rounded 1c", sans-serif;
    font-weight: 800;
    color: var(--title);
    line-height: 1;
  }
  .title__line { display: block; }
  .title__line--top { font-size: 112px; letter-spacing: 4px; }
  .title__line--main { font-size: 138px; letter-spacing: 22px; margin-top: 42px; }
  .bulb {
    position: absolute; left: 350px; top: 4px;
    width: 110px; height: 160px;
    border-radius: 55px 55px 20px 20px;
    background: radial-gradient(circle at 50% 35%, #f8d86a 0%, #f0b53a 55%, rgba(240,181,58,0) 75%);
  }
  .publisher {
    position: absolute; left: 545px; top: 34px;
    color: var(--white);
    font-weight: 700; font-size: 17px;
  }
  .publisher__head { display: flex; gap: 14px; margin-bottom: 10px; font-size: 18px; }
  .publisher__label { color: var(--yellow); }
  .offices { display: grid; grid-template-columns: 58px 300px auto; row-gap: 4px; font-size: 16px; font-weight: 500; }
  .offices dt { color: var(--yellow); font-weight: 700; }
  .issue {
    position: absolute; left: 378px; top: 336px;
    width: 116px; height: 116px; border-radius: 50%;
    background: radial-gradient(circle at 40% 35%, #e9f7a0 0%, var(--lime) 60%, #8fbf1f 100%);
    border: 6px solid var(--white);
    display: flex; align-items: center; justify-content: center;
    font-family: "M PLUS Rounded 1c", sans-serif; font-weight: 800;
    font-size: 60px; color: var(--green-deep);
  }
  .contents {
    position: absolute; left: 512px; top: 346px;
    width: 658px; height: 116px;
    background: var(--white);
    border-radius: 10px 58px 58px 10px;
    padding: 10px 30px 10px 34px;
    list-style: none;
    display: flex; flex-direction: column; justify-content: space-between;
  }
  .contents__item {
    display: grid; grid-template-columns: 22px 1fr 74px;
    font-size: 16px; font-weight: 500; color: var(--ink); line-height: 1.3;
  }
  .contents__item::before { content: "★"; color: var(--star); }
  .issue-date {
    position: absolute; left: 54px; top: 441px;
    font-size: 17px; font-weight: 700; color: var(--white);
  }
  .issue-date__label { color: var(--yellow); margin-right: 8px; }
</style>
</head>
<body>
<header class="masthead">
  <div class="masthead__texture"></div>

  <h1 class="title">
    <span class="title__line title__line--top">未来</span>
    <span class="title__line title__line--main">TSUBASA報</span>
  </h1>

  <div class="bulb" role="img" aria-label="電球のイラスト"></div>

  <div class="publisher">
    <p class="publisher__head"><span class="publisher__label">発 行</span><span>株式会社青葉企画舎 https://www.aobakikakusha-news.jp/</span></p>
    <dl class="offices">
      <dt>東　京</dt><dd>中央区日本橋浜町3-5-8</dd><dd>TEL:03-4417-2968</dd>
      <dt>大　阪</dt><dd>大阪市西区江戸堀3-7-21</dd><dd>TEL:06-7142-8867</dd>
      <dt>名古屋</dt><dd>安城市御幸本町4-16-8</dd><dd>TEL:0566-47-2139</dd>
    </dl>
  </div>

  <div class="issue" aria-label="第27号">27</div>

  <ul class="contents">
    <li class="contents__item"><span>脱炭素・SDGsからみた日本企業の技術ポテンシャル</span><span>2面</span></li>
    <li class="contents__item"><span>ブックステーション</span><span>2・3面</span></li>
    <li class="contents__item"><span>御食国から物申す〜連載 第15回〜</span><span>3面</span></li>
    <li class="contents__item"><span>お家時間を充実させるおすすめグッズ</span><span>4面</span></li>
  </ul>

  <p class="issue-date"><span class="issue-date__label">発行日</span>2022年3月23日</p>
</header>
</body>
</html>
```